Rusty Lantern Ale Room & Sports Kitchen Menu

This is my dine in menu for my sports bar. I would like it to be playful and fun. The colors of my logo are also the colors of my bar. You can look at facebook or rustylanternaleroom.com to see pictures. My current menu is a trifold and I would like to move away from that design. I like a the menu to flow, but am very open to new concepts. I feel like my current one is too boring and not professional enough as well as not catchy. I like a colored page, with colored lettering not necessarily black or white text. I currently use the colors of my log on my menu but like the idea of something that is not boring.

Target Market(s)

customers coming into my bar

Industry/Entity Type

Sports Bar

Requirements
Must have
• LOGO, Specials,
Nice to have
• pictures of food
Should not have
• open to all designs

```html
<!DOCTYPE html>
<html lang="en">
<head>
<meta charset="utf-8">
<title>Rusty Lantern Ale Room &amp; Sports Kitchen – Menu</title>
<link rel="stylesheet" href="https://fonts.googleapis.com/css2?family=Rye&family=Oswald:wght@400;500&family=Josefin+Sans:wght@600;700&family=Kaushan+Script&family=Bebas+Neue&family=Special+Elite&display=swap">
<style>
:root{
  --slate:#59636a;
  --slate-dark:#454e55;
  --slate-light:#6c767b;
  --amber:#e9982d;
  --amber-deep:#c97a1a;
  --chalk:#f1efe6;
}
*{margin:0;padding:0;box-sizing:border-box}
html,body{width:1200px;height:934px;overflow:hidden}
body{background:var(--slate-dark)}
.menu{position:relative;width:1200px;height:934px;overflow:hidden;
  background:radial-gradient(ellipse at 50% 45%,var(--slate-light),var(--slate) 55%,var(--slate-dark));
  color:var(--chalk);font-family:"Josefin Sans",sans-serif;font-weight:700;text-transform:uppercase}
.block{position:absolute}
.amber{color:var(--amber)}
.head-slab{font-family:"Rye",serif;color:var(--amber);font-weight:400;letter-spacing:2px}
.head-script{font-family:"Kaushan Script",cursive;color:var(--amber);font-weight:400;text-transform:none}
.head-tall{font-family:"Bebas Neue",sans-serif;color:var(--amber);font-weight:400}
.rule{height:2px;background:var(--chalk);opacity:.85}
.item{margin-bottom:7px}
.item-name{font-family:"Special Elite",monospace;color:var(--amber);font-weight:400;line-height:1}
.desc{font-size:6.4px;line-height:1.35;letter-spacing:.1px}
.photo{position:absolute;border-radius:50%;border:3px solid var(--amber)}

/* starters */
.starters-title{left:190px;top:36px;font-size:44px}
.starters-rule{left:200px;top:86px;width:242px}
.starters-col .item-name{font-size:11.5px}
.starters-col .desc{font-size:6.2px}
.price-list p{font-family:"Special Elite",monospace;color:var(--amber);font-size:10px;line-height:1.35;font-weight:400}
.price-list span{color:var(--chalk);font-family:"Josefin Sans",sans-serif;font-weight:700;font-size:7px}

/* wings */
.wings-title{left:694px;top:32px;font-size:42px;line-height:.85;text-align:left}
.wings-center{left:616px;width:282px;text-align:center}
.wings-center .item-name{font-size:15px;font-family:"Bebas Neue",sans-serif;letter-spacing:1px}
.wings-center .desc{font-size:6.6px}

/* sandwiches */
.sandwich-col{left:918px;top:108px;width:256px}
.sandwich-col .item-name{font-size:13.5px}
.sandwich-col .desc{font-size:6.6px}

/* philly */
.philly-title{left:36px;top:300px;width:490px;text-align:center}
.philly-title .big{font-family:"Rye",serif;font-size:36px;color:var(--amber);font-weight:400;line-height:1}
.philly-title .spaced{font-family:"Rye",serif;font-size:18px;color:var(--amber);letter-spacing:13px;font-weight:400;margin-top:2px}
.philly-body{left:36px;top:388px;width:528px;font-size:10.2px;line-height:1.35}
.philly-item{text-align:center;margin-top:6px}
.philly-item .item-name{font-size:15px}
.philly-item p{font-size:10.2px;line-height:1.4}

/* cold subs */
.subs-title{left:196px;top:556px;width:220px}
.subs-title .script{font-size:40px;line-height:1}
.subs-title .tall{font-size:48px;line-height:.9;letter-spacing:1px}
.subs-rule{left:190px;top:654px;width:246px}
.subs-body{left:36px;top:668px;width:528px;text-align:center;font-size:7.6px;line-height:1.4}
.subs-grid{left:40px;top:766px;width:520px;display:grid;grid-template-columns:290px 230px;row-gap:6px}
.subs-grid .item-name{font-size:13.5px}
.subs-grid .desc{font-size:7.4px}

/* lantern style box */
.style-box{left:616px;top:342px;width:271px;height:294px;border:2px solid var(--amber);outline:1px solid var(--amber);outline-offset:-6px;text-align:center;padding:18px 14px 0}
.style-box .mark{margin:0 auto 4px;width:62px;height:48px;background:var(--amber);border-radius:50%}
.style-box .big{font-family:"Josefin Sans",sans-serif;color:var(--amber);font-size:34px;line-height:1}
.style-box .spaced{color:var(--amber);font-size:15px;letter-spacing:10px;font-family:"Special Elite",monospace;margin-top:2px}
.style-box .desc{font-size:6.6px;margin-top:6px}
.style-box .item-name{font-size:13px;margin-top:6px}

/* salads */
.salads-title{left:616px;top:644px;width:282px;text-align:center;font-size:40px}
.salads-body{left:616px;top:694px;width:282px;text-align:center}
.salads-body .item-name{font-size:13px}
.salads-body .desc{font-size:6.6px}

/* burgers */
.burgers-title{left:976px;top:462px;font-size:40px;letter-spacing:1px}
.burgers-body{left:918px;top:506px;width:254px;text-align:center}
.burgers-body .intro{font-size:8px;line-height:1.5;text-align:justify}
.burgers-body .item-name{font-size:13.5px;margin-top:6px}
.burgers-body .desc{font-size:7.8px;line-height:1.45}
</style>
</head>
<body>
<main class="menu" aria-label="Rusty Lantern Ale Room &amp; Sports Kitchen menu">

  <!-- STARTERS -->
  <h2 class="block head-slab starters-title">STARTERS</h2>
  <div class="block rule starters-rule"></div>

  <section class="block starters-col" style="left:36px;top:106px;width:170px">
    <div class="item"><h3 class="item-name">Philly Quesadilla</h3><p class="desc">Your choice of philly chicken or steak &amp; onions, cheddar cheese, jalapenos, side of salsa &amp; sour cream<br>– 10.95</p></div>
    <div class="item"><h3 class="item-name">Philly Nachos</h3><p class="desc">Nacho chips covered with your choice of philly chicken or steak meat &amp; onions, jalapenos &amp; queso cheese.<br>– 10.95</p></div>
    <div class="item"><h3 class="item-name">Philly Tater Tots</h3><p class="desc">Your choice of philly steak or chicken on tater tots covered with cheese whip.<br><br>– 10.95</p></div>
  </section>

  <section class="block starters-col" style="left:216px;top:106px;width:164px">
    <div class="item"><h3 class="item-name">Jalapeno &amp; Cheddar Pierogies (6)</h3><p class="desc">These delectable little dumplings are stuffed with creamy mashed potatoes, cheddar &amp; jalapenos then deep-fried to perfection &amp; seasoned.<br>– 7.95</p></div>
    <div class="item"><h3 class="item-name">Provolone Cheese Sticks (6)</h3><p class="desc">Served with marinara<br>– 8.49</p></div>
    <div class="item"><h3 class="item-name">Potato Skins (6)</h3><p class="desc">Bacon, chives, &amp; cheese whip or cheddar cheese (+$.50) with a side of sour cream<br>– 7.95<br><span style="font-size:5px">Add chicken philly meat or philly steak – 4.50</span></p></div>
  </section>

  <section class="block starters-col price-list" style="left:398px;top:106px;width:172px">
    <div class="item"><h3 class="item-name">Sampler Platter</h3><p class="desc" style="font-family:'Josefin Sans',sans-serif;color:var(--chalk);font-size:6.2px;line-height:1.35">Provolone sticks (4), boneless wings (6), pierogies (3), &amp; chips with queso.<br>– 14.95</p></div>
    <p>Popcorn Shrimp w/ Fries <span>– 8.49</span></p>
    <p>Chips &amp; Queso <span>– 6.49</span></p>
    <p>Queso Refill <span>– 2.00</span></p>
    <p>Chip Refill <span>– 1.00</span></p>
    <p>Mini Corn Dogs (12) <span>– 6.49</span></p>
    <p>Basket of Fries <span>– 2.99</span></p>
    <p>Onion Rings <span>– 6.49</span></p>
  </section>

  <!-- JUMBO WINGS -->
  <div class="photo" role="img" aria-label="Photo of saucy jumbo chicken wings on a plate" style="left:576px;top:30px;width:108px;height:108px;background:radial-gradient(circle at 45% 45%,#c85a22,#9b3a16 45%,#d9d6cf 62%,#b9b6ae)"></div>
  <h2 class="block head-tall wings-title">JUMBO<br>&nbsp;&nbsp;&nbsp;WINGS</h2>
  <p class="block desc" style="left:656px;top:118px;width:230px;font-size:6.6px">Add a side of fries or chips with wings – 2.00</p>
  <p class="block desc" style="left:626px;top:138px;width:260px;font-size:6.4px;text-align:center">Finally wings with some meat on them!<br>Wings are jointed wings, a flat and drumstick together.</p>
  <section class="block wings-center" style="top:166px">
    <div class="item"><h3 class="item-name">Jumbo Traditional Wings</h3><p class="desc">3 jointed wings (3 flats &amp; 3 drums) – 8.95<br>6 jointed wings (6 flats &amp; 6 drums) – 16.95</p></div>
    <div class="item"><h3 class="item-name">Boneless Wings</h3><p class="desc">12 wings – 8.95<br>24 wings – 17.95</p></div>
    <div class="item"><h3 class="item-name">Chicken Tender (4) Basket</h3><p class="desc">w/fries or chips – 12.95</p></div>
    <p class="desc" style="margin-top:8px">Sauce choices:<br>Bourbon BBQ, medium, Thai zing,<br>mango habanero, hot (with jalapeno),<br>scorchin' (with habanero peppers),<br>Lantern Punch (with ghost peppers)</p>
  </section>

  <!-- SANDWICHES -->
  <h2 class="block head-script" style="left:946px;top:30px;font-size:40px">Sandwiches</h2>
  <section class="block sandwich-col">
    <p class="desc" style="margin-bottom:8px;font-size:7.6px">All sandwiches come on a sub roll &amp; served with fries or chips</p>
    <div class="item"><h3 class="item-name">Italian Sausage</h3><p class="desc">½ pound of sausage covered with onions and bell peppers on a hoagie roll. You can't resist my Italian sausage! – 10.95</p></div>
    <div class="item"><h3 class="item-name">Bacon &amp; Jalapeno Grilled Cheese</h3><p class="desc">Half pound of bacon (6 slices) – 10.95</p></div>
    <div class="item"><h3 class="item-name">Buffalo Ranch Chicken Sandwich</h3><p class="desc">Ranch and medium sauce on a breaded chicken breast<br>– 10.95</p></div>
    <div class="item"><h3 class="item-name">Grilled Chicken Sandwich</h3><p class="desc">(8 oz) – 10.95</p></div>
    <div class="item"><h3 class="item-name">Gyro</h3><p class="desc">Gyro meat on the best pita bread you'll ever have. The meat is smothered in our soon to be famous tzatziki sauce. – 10.95</p></div>
    <div class="item"><h3 class="item-name">Lantern Dog</h3><p class="desc">This is our version of a coney dog. A deep fried beef frank on a Marrone roll topped with our guy Marco's coney meat sauce, shredded cheddar, raw onions, pepperoncinis, &amp; jalapenos. - 9.95</p></div>
  </section>

  <!-- ORIGINAL PHILLY -->
  <div class="block philly-title">
    <h2 class="big">ORIGINAL PHILLY</h2>
    <p class="spaced">CHEESESTEAKS</p>
  </div>
  <div class="block rule" style="left:136px;top:372px;width:300px;height:1.5px"></div>
  <section class="block philly-body">
    <p>Made with shaved ribeye on the world famous Marrone roll. Comes with fries or chips, add whatever toppings you want: pepper relish, mushrooms, bell peppers, pepperoncinis, jalapenos, marinara, or hoagie style (lettuce, tomato, &amp; mayo) – .75ea</p>
    <div class="philly-item"><h3 class="item-name">Famous Philly</h3><p>Shaved steak, grilled onions &amp; white american cheese,<br>provolone, or cheese whip – 10.95</p></div>
    <div class="philly-item"><h3 class="item-name">Chicken Philly</h3><p>Chopped chicken, grilled onions &amp; white american cheese,<br>provolone, or cheese whip – 10.95</p></div>
  </section>

  <!-- GOURMET COLD SUBS -->
  <div class="photo" role="img" aria-label="Photo of a loaded sub sandwich with fries" style="left:18px;top:532px;width:156px;height:132px;border-radius:50%;background:radial-gradient(ellipse at 50% 55%,#d9a13d,#9a5a2a 40%,#c9c4b6 65%,#8f8c84)"></div>
  <div class="block subs-title">
    <h2 class="head-script script">Gourmet</h2>
    <h2 class="head-tall tall">COLD SUBS</h2>
  </div>
  <div class="block rule subs-rule"></div>
  <section class="block subs-body">
    <p>All subs come with approximately ½ pound of meat and cheese plus toppings. These meats are high end and not processed.</p>
    <p style="margin-top:8px">"House way" is with lettuce, tomato, red onion, oil, red wine vinegar, mayo, salt, pepper, and oregano. Rolls cooked fresh!!!</p>
    <p style="margin-top:8px">Includes fries or fresh cooked chips<br>Add jalapeno, pepperoncini, pepper relish, bell peppers – .75ea</p>
  </section>
  <section class="block subs-grid">
    <div class="item"><h3 class="item-name">The Grinder Deluxe</h3><p class="desc">Provolone, ham, prosciutto, capicola,<br>salami – 10.95</p></div>
    <div class="item"><h3 class="item-name">Club Sub</h3><p class="desc">Provolone, ham, turkey, bacon – 10.95</p></div>
    <div class="item"><h3 class="item-name">Turkey Sub</h3><p class="desc">Provolone, real turkey breast – 10.95</p></div>
    <div class="item"><h3 class="item-name">Roast Beef Sub</h3><p class="desc">Provolone, roast beef (med rare) – 11.95</p></div>
    <div class="item"><h3 class="item-name">Pastrami (Cold or Hot)</h3><p class="desc">Provolone, pastrami – 10.95</p></div>
    <div class="item"><h3 class="item-name">BLT</h3><p class="desc">Half pound of bacon (6 slices) – 10.95<br>One pound of bacon (12 slices) – 15.95</p></div>
  </section>

  <!-- LANTERN STYLE -->
  <section class="block style-box">
    <div class="mark" aria-hidden="true"></div>
    <h2 class="big">LANTERN</h2>
    <p class="spaced">-STYLE-</p>
    <p class="desc">(The fries come on the sub, not on the side!)</p>
    <p class="desc" style="text-align:left">These subs come on a hogie roll that is not toasted. The meat is thrown on the grill for a minute to heat it up a little and then they are covered with french fries, provolone cheese, and our soon to be famous pepper relish coleslaw. It's a one of a kind taste with a little kick!</p>
    <h3 class="item-name">Pastrami</h3>
    <p class="desc" style="margin-top:1px">Our premium pastrami is shipped in from back east!<br>You're going to love it!. – 11.95</p>
    <h3 class="item-name">Prime Rib</h3>
    <p class="desc" style="margin-top:1px">Shaved prime rib that will melt in your mouth. – 13.95</p>
    <h3 class="item-name" style="margin-top:2px">Roast Beef</h3>
    <p class="desc" style="margin-top:1px">A very high quality roast beef. – 11.95</p>
  </section>

  <!-- SALADS -->
  <h2 class="block head-script salads-title">Salads</h2>
  <section class="block salads-body">
    <p class="desc" style="margin-bottom:6px">Ranch, greek feta, blue cheese, italian, 1000 island</p>
    <div class="item"><h3 class="item-name">Chicken Tender Salad</h3><p class="desc">Sliced chicken tenders served over sliced lettuce, topped with tomatoes, shredded cheddar, cucumbers, red onions, &amp; croutons. – 10.95</p></div>
    <div class="item"><h3 class="item-name">Grilled Chicken Salad</h3><p class="desc">Seasoned and grilled chicken breast served over sliced lettuce, topped with tomatoes, shredded cheddar, cucumbers, red onions, &amp; croutons. – 10.95</p></div>
    <div class="item"><h3 class="item-name">Chef Salad</h3><p class="desc">Ham and turkey served over sliced lettuce, topped with tomatoes, shredded cheddar cheese, cucumbers, red onions, hardboiled egg, &amp; croutons – 10.95</p></div>
    <div class="item"><h3 class="item-name">Gyro Salad</h3><p class="desc">Gyro meat covered in tzatziki sauce served over sliced lettuce, topped with tomatoes, shredded cheddar, cucumbers, red onions, &amp; croutons. – 10.95</p></div>
  </section>

  <!-- BURGERS -->
  <div class="photo" role="img" aria-label="Photo of a bacon cheeseburger with chips" style="left:872px;top:412px;width:116px;height:92px;background:radial-gradient(ellipse at 45% 50%,#b5482a,#7a3a1e 35%,#d8b25a 55%,#c9c4b6 72%)"></div>
  <h2 class="block head-tall burgers-title">BURGERS</h2>
  <section class="block burgers-body">
    <p class="intro">Choice of american, cheddar, swiss, pepper jack, provolone brioche bun or sub roll bun, come with a side of fries or chips. (lettuce/tomatoes/pickles on request only)</p>
    <h3 class="item-name" style="margin-top:22px">Ground Bacon Burger w/ Cheese</h3>
    <p class="desc">One third pound burger is 70% ground bacon &amp; 30% beef. It's covered with your choice of cheese and 3 strips of bacon. – 10.95</p>
    <h3 class="item-name" style="margin-top:10px">Cheeseburger</h3>
    <p class="desc">Quarter pound burger topped with your choice of cheese.<br>Single – 7.95 &nbsp;&nbsp;&nbsp;&nbsp; Double – 9.95</p>
    <h3 class="item-name" style="margin-top:18px">Italian Cheeseburger</h3>
    <p class="desc">Quarter pound burger topped with capicola &amp; your choice of cheese. – 11.95</p>
    <h3 class="item-name" style="margin-top:8px">Pastrami Cheeseburger</h3>
    <p class="desc">Quarter pound burger topped with pastrami &amp; your choice of cheese. – 11.95</p>
    <h3 class="item-name" style="margin-top:8px">Bad A$$ Philly Burger</h3>
    <p class="desc" style="text-align:justify">Two ¼ lb patties topped with american cheese. On top of the patties you will find philly meat, grilled onions, &amp; more american cheese. You get the best of both worlds, a burger and a philly put together on a sub roll, get the napkins ready, you're in for a treat!!!! – 15.95</p>
  </section>

</main>
</body>
</html>
```